Completely Coded Dog Community Website - Mobile Centric & Highly Responsive

We need a completely coded design based in Wordpress CMS that is designed with mobile in mind first! I would like to carry over the style of our current website (brightkennel.c0m) into the design of the responsive website. In addition, please only submit designs if you provide high quality admin support, as the winning design will likely be hired to provide monthly support forward at $100/month (SEO skill set valued). Also am looking for a quote on an iphone and android app so please submit designs only if you have capability to create the highest quality apps. No cheap looking template submissions please...will need form, chat, sign in and e-commerce integration. I have vector files if needed for website.
Updates

Project Deadline Extended
Reason: Want to see more mobile friendly, modern designs and responses to willingness for web admin support going forward. Thanks

Target Market(s)

Adults based in the USA aged 25-50 that own dogs

Industry/Entity Type

E-Commerce

Requirements
Must have
• Pages:
Home Page
About Us
Contact Us
Dog Deals
Videos
Photos
Health
Training
Breeds
Ask the Dog Expert
Dog Product Reviews
Dog Stories
Dog Friendly Travel
Dog Care
Contests
Nice to have
• SEO
Metatags
Unique page layouts
Social integration to our social media accounts
Social API logins
Should not have
• Cheap template look
Not consistent with previous color scheme
Different logo than our current options

```html
<!DOCTYPE html>
<html lang="en">
<head>
<meta charset="utf-8">
<title>BrightKennel – Dog Community</title>
<link rel="stylesheet" href="https://fonts.googleapis.com/css2?family=Roboto:wght@300;400;500;700&family=Oswald:wght@500&display=swap">
<style>
:root{
  --sky:#bfe6f6;
  --sky-deep:#8fd2ee;
  --orange:#f7941d;
  --orange-dark:#e8771a;
  --nav-text:#2a2a2a;
  --nav-active:#1a7fb8;
  --card-border:#8ec8e8;
  --card-top:#eaf6fc;
  --card-bottom:#bfe3f5;
  --ink:#1d1d1d;
  --body:#3a3a3a;
  --teal:#2f6f86;
  --footer:#3f86be;
  --white:#ffffff;
  --hero-blue:#2a86c9;
}
*{box-sizing:border-box;margin:0;padding:0}
html,body{width:695px;height:1200px;overflow:hidden}
body{position:relative;background:var(--white);font-family:'Roboto',Arial,sans-serif;color:var(--ink)}
.abs{position:absolute}

.masthead{left:0;top:0;width:695px;height:300px;
  background:linear-gradient(180deg,var(--sky-deep) 0%,#d3eef9 60%,var(--white) 100%)}
.logo{left:0;top:46px;width:695px;text-align:center;font-weight:700;font-size:16px;color:var(--hero-blue);letter-spacing:.2px}
.logo .dot{display:inline-block;width:12px;height:12px;border-radius:50%;background:var(--orange);vertical-align:-1px;margin-right:5px}

.main-nav{left:0;top:78px;width:695px;height:32px;background:var(--orange);
  border-top:1px dashed #ffd08a;border-bottom:1px dashed #ffd08a;
  display:flex;align-items:center;padding-left:43px;gap:0}
.main-nav a{font-size:7.4px;color:var(--nav-text);text-decoration:none;margin-right:16.5px;text-transform:uppercase}
.main-nav a.active{color:var(--nav-active)}

.hero{left:43px;top:112px;width:609px;height:229px;border:2px solid #5aa6d8;
  background:linear-gradient(90deg,#b8bec3 0%,#e4e6e8 45%,#f2f2f2 100%);overflow:hidden}
.hero-photo{left:230px;top:0;width:377px;height:225px;
  background:radial-gradient(ellipse at 50% 55%,#e8c28a 0%,#d3a466 35%,rgba(220,220,220,0) 72%)}
.hero-title{left:18px;top:32px;font-family:'Oswald',Arial,sans-serif;font-weight:500;font-size:31px;line-height:36px;color:var(--hero-blue);letter-spacing:-.5px}
.hero-text{left:19px;top:110px;width:230px;font-size:9.4px;line-height:13px;color:#222}
.hero .btn{left:19px;top:156px}
.dots{left:18px;top:206px;display:flex;gap:4px}
.dots span{width:6px;height:6px;border-radius:50%;background:#222}
.dots span:first-child{background:#9fd5f0}

.btn{display:inline-block;background:var(--orange-dark);color:var(--white);font-size:6.8px;font-weight:500;
  text-transform:uppercase;padding:0 11px;height:18px;line-height:18px;text-decoration:none}

.card{width:191px;height:105px;border:1.5px solid var(--card-border);
  background:linear-gradient(180deg,var(--card-top),var(--card-bottom));overflow:hidden}
.card .pic{position:absolute;right:0;top:0;width:92px;height:100%}
.card h3{position:absolute;left:11px;top:13px;font-weight:400;font-size:15px;line-height:19px;text-transform:uppercase;color:var(--ink);z-index:1}
.card p{position:absolute;left:13px;top:52px;font-size:6.6px;line-height:10.5px;color:#333;z-index:1}
.card .btn{position:absolute;left:13px;top:77px}
.card.short h3{top:14px}
.card.short p{top:34px}
.card.short .btn{top:60px}
.card.low{height:95px}

.about{left:0;top:608px;width:695px;height:153px;background:var(--teal)}
.about-photo{left:43px;top:16px;width:191px;height:122px;background:linear-gradient(135deg,#7fb23a,#b9c98a 55%,#e6e0d0)}
.about h2{left:250px;top:17px;width:410px;text-align:center;font-weight:400;font-size:14.5px;color:var(--white)}
.about p{left:255px;top:42px;width:400px;text-align:center;font-weight:300;font-size:7.1px;line-height:12.3px;color:#d9eaf1}
.about .btn{left:423px;top:120px}

.sec-title{font-weight:500;font-size:14px;color:var(--ink);top:780px}
.thumb{width:92px;height:54px}
.contest-text{left:460px;top:884px;width:192px;font-size:7.1px;line-height:12.3px;color:#333}

.site-footer{left:0;top:1044px;width:695px;height:156px;background:var(--footer);color:var(--white)}
.site-footer h4{position:absolute;top:17px;font-weight:400;font-size:9.5px;text-transform:uppercase;letter-spacing:.2px}
.site-footer ul{position:absolute;list-style:none;font-size:6.9px;line-height:14.4px}
.contact-block{left:220px;top:39px;font-size:6.9px;line-height:11.6px}
.contact-block b{font-weight:700}
.social{left:357px;top:39px;list-style:none}
.social li{display:flex;align-items:center;height:22.4px;font-size:7px}
.social .ic{width:17px;height:17px;border-radius:50%;background:#2d5f9a;border:2px solid var(--white);margin-right:9px}
.field{position:absolute;left:512px;width:141px;height:19px;background:var(--white);font-size:6.5px;font-style:italic;color:#666;padding:6px 8px}
.site-footer .btn{position:absolute;left:590px;top:79px;height:19px;line-height:19px;padding:0 12px}
.copyright{left:512px;top:114px;font-size:6.7px;line-height:11.5px;color:#cfe3f3}
</style>
</head>
<body>

<div class="abs masthead"></div>
<div class="abs logo"><span class="dot"></span>BrightKennel.c0m</div>

<nav class="abs main-nav">
  <a class="active" href="#">Home</a><a href="#">About Us</a><a href="#">Dog Deals</a><a href="#">Videos</a><a href="#">Photos</a><a href="#">Dog Stories</a><a href="#">Training</a><a href="#">Ask the Dog Expert</a><a href="#">Dog Care</a><a href="#">Contests</a><a href="#">Contact Us</a>
</nav>

<section class="abs hero">
  <div class="abs hero-photo" role="img" aria-label="Three golden retriever puppies lying side by side"></div>
  <h1 class="abs hero-title">Sit aspernatur aut<br>odit aut fugit..</h1>
  <p class="abs hero-text">Sed ut perspiciatis unde omnis iste natus error sit voluptatem accusantium dolorem- que laudantium, totam rem aperiam.</p>
  <a class="abs btn" href="#">Read More</a>
  <div class="abs dots"><span></span><span></span><span></span><span></span></div>
</section>

<div class="abs card" style="left:43px;top:363px">
  <div class="pic" role="img" aria-label="Two large dogs giving a high five" style="background:linear-gradient(90deg,rgba(0,0,0,0),#8a6a4a 40%,#b78a55)"></div>
  <h3>Dog<br>Deals</h3>
  <p>Veritatis et quasi architecto<br>beatae vitae dicta sunt explicabo.</p>
  <a class="btn" href="#">Read More</a>
</div>
<div class="abs card" style="left:252px;top:363px">
  <div class="pic" role="img" aria-label="Dog expert crouching with several puppies" style="background:linear-gradient(90deg,rgba(0,0,0,0),#7a5a3c 40%,#d9c6a4)"></div>
  <h3>Ask the<br>Dog Expert</h3>
  <p>Veritatis et quasi architecto<br>beatae vitae dicta sunt explicabo.</p>
  <a class="btn" href="#">Read More</a>
</div>
<div class="abs card" style="left:462px;top:363px">
  <div class="pic" role="img" aria-label="Small dog in sunglasses sitting on a blue suitcase" style="background:linear-gradient(90deg,rgba(0,0,0,0),#7fc4e8 45%,#3aa0d8)"></div>
  <h3>Dog Friendly<br>Travel</h3>
  <p>Veritatis et quasi architecto<br>beatae vitae dicta sunt explicabo.</p>
  <a class="btn" href="#">Read More</a>
</div>

<div class="abs card" style="left:43px;top:484px">
  <div class="pic" role="img" aria-label="Package of dog treats" style="background:linear-gradient(90deg,rgba(0,0,0,0),#3f8a3a 45%,#5aa048)"></div>
  <h3>Dog Product<br>Reviews</h3>
  <p>Veritatis et quasi architecto<br>beatae vitae dicta sunt explicabo.</p>
  <a class="btn" href="#">Read More</a>
</div>
<div class="abs card" style="left:252px;top:484px">
  <div class="pic" role="img" aria-label="Golden retriever lying down" style="background:linear-gradient(90deg,rgba(0,0,0,0),#c88a3e 45%,#b07028)"></div>
  <h3>Dog<br>Stories</h3>
  <p>Veritatis et quasi architecto<br>beatae vitae dicta sunt explicabo.</p>
  <a class="btn" href="#">Read More</a>
</div>
<div class="abs card" style="left:462px;top:484px">
  <div class="pic" role="img" aria-label="Small dog wrapped in a pink towel" style="background:linear-gradient(90deg,rgba(0,0,0,0),#f1e4e2 45%,#e9c6c4)"></div>
  <h3>Dog<br>Care</h3>
  <p>Veritatis et quasi architecto<br>beatae vitae dicta sunt explicabo.</p>
  <a class="btn" href="#">Read More</a>
</div>

<section class="abs about">
  <div class="abs about-photo" role="img" aria-label="Smiling man hugging a white dog on grass"></div>
  <h2 class="abs">ABOUT US</h2>
  <p class="abs">Aliquam molestie, mi et imperdiet euismod, dui purus auctor tellus, et interdum lacus lectus et ante. Sed accumsan sollicitudin sapien, sit amet adipiscing turpis gravida ac. In congue, neque ac lobortis volutpat, libero mauris varius mi, vitae suscipit ipsum ligula vitae risus. Duis aliquam nibh a dui iaculis viverra id a velit. Vivamus egestas risus in magna varius commodo. Sed semper viverra egestas. Etiam pretium porttitor lectus, vel ornare neque porta volutpat.</p>
  <a class="abs btn" href="#">Read More</a>
</section>

<h2 class="abs sec-title" style="left:43px">PHOTOS</h2>
<h2 class="abs sec-title" style="left:251px">VIDEOS</h2>
<h2 class="abs sec-title" style="left:459px">CONTESTS</h2>

<div class="abs thumb" role="img" aria-label="Golden retriever portrait" style="left:43px;top:802px;background:linear-gradient(135deg,#6b4a2a,#d39a4c)"></div>
<div class="abs thumb" role="img" aria-label="French bulldog on white" style="left:142px;top:802px;background:radial-gradient(circle at 50% 55%,#8a8a8a,#f4f4f4 60%)"></div>
<div class="abs thumb" role="img" aria-label="White puppy on grass" style="left:43px;top:864px;background:linear-gradient(160deg,#9cc46a,#e8e4c8 55%,#7aa840)"></div>
<div class="abs thumb" role="img" aria-label="Puppies in a wicker basket" style="left:142px;top:864px;background:linear-gradient(180deg,#3e2c1c,#a87a44 60%,#6a4a2a)"></div>

<div class="abs" role="img" aria-label="Puppy running on grass, video preview" style="left:251px;top:802px;width:193px;height:116px;background:linear-gradient(180deg,#8a7a5a,#d9c8a6 45%,#6f8a3e)"></div>
<svg class="abs" style="left:329px;top:842px" width="36" height="36" viewBox="0 0 36 36" aria-hidden="true">
  <circle cx="18" cy="18" r="16" fill="none" stroke="#fff" stroke-width="2.5"/>
  <path d="M14 10 L26 18 L14 26 Z" fill="#fff"/>
</svg>

<div class="abs" role="img" aria-label="Dog leaping over an agility hurdle" style="left:460px;top:802px;width:192px;height:76px;background:linear-gradient(180deg,#8a8a6a,#6f8a4a 60%,#4a6a2a)"></div>
<p class="abs contest-text">Aliquam molestie, mi et imperdiet euismod, dui purus auctor tellus, et interdum lacus lectus et ante. Sed accumsan sollicitudin sapien..</p>

<div class="abs card short low" style="left:43px;top:936px">
  <div class="pic" role="img" aria-label="Veterinarian holding a small dog" style="background:linear-gradient(90deg,rgba(0,0,0,0),#e9eef2 45%,#c49060)"></div>
  <h3>Health</h3>
  <p>Veritatis et quasi architecto<br>beatae vitae dicta sunt explicabo.</p>
  <a class="btn" href="#">Read More</a>
</div>
<div class="abs card short low" style="left:252px;top:936px">
  <div class="pic" role="img" aria-label="Trainer kneeling with a jumping dog" style="background:linear-gradient(90deg,rgba(0,0,0,0),#6a7a9a 45%,#a8683a)"></div>
  <h3>Training</h3>
  <p>Veritatis et quasi architecto<br>beatae vitae dicta sunt explicabo.</p>
  <a class="btn" href="#">Read More</a>
</div>
<div class="abs card short low" style="left:462px;top:936px">
  <div class="pic" role="img" aria-label="Golden retrievers in a meadow" style="background:linear-gradient(180deg,#2f6fb0,#e6dcc0 60%,#6a9a3a)"></div>
  <h3>Breeds</h3>
  <p>Veritatis et quasi architecto<br>beatae vitae dicta sunt explicabo.</p>
  <a class="btn" href="#">Read More</a>
</div>

<footer class="abs site-footer">
  <h4 style="left:43px">Navigation</h4>
  <ul style="left:43px;top:35px"><li>About Us</li><li>Contact Us</li><li>Dog Deals</li><li>Videos</li><li>Photos</li><li>Health</li></ul>
  <ul style="left:114px;top:35px"><li>Training</li><li>Breeds</li><li>Ask the Dog Expert</li><li>Dog Product Reviews</li><li>Dog Stories</li><li>Dog Friendly Travel</li><li>Dog Care</li><li>Contests</li></ul>

  <h4 style="left:220px">Contact Us</h4>
  <div class="abs contact-block">
    <b>BRIGHT KENNEL</b><br>412 Alder Lane<br>Glasgow, G12 8QT<br><span style="line-height:22px">Ph: 555-014-2290</span><br><span style="position:relative;top:-5px">Email: info@brightkennel.c0m</span>
  </div>

  <h4 style="left:357px">Follow Us</h4>
  <ul class="abs social">
    <li><span class="ic"></span>Pawbook</li>
    <li><span class="ic" style="background:#2a8fd6"></span>Chirper</li>
    <li><span class="ic" style="background:#c8232c"></span>Pinboard</li>
    <li><span class="ic" style="background:#d44132"></span>Circles</li>
    <li><span class="ic" style="background:#1d5f9a"></span>Dugout</li>
  </ul>

  <h4 style="left:512px">Newsletter Sign Up</h4>
  <div class="field" style="top:34px">Enter Name</div>
  <div class="field" style="top:56px">Enter Email Address</div>
  <a class="btn" href="#">Subscribe</a>
  <p class="abs copyright">Copyright © 2015. Company Name<br>All Right Reserved</p>
</footer>

</body>
</html>
```